Business card por a urban DJ, up scale audience target

Need a sober design, modern, conservative colors but i can consider some options, y play rnb, hip hop, EDM and top40.

Business card for contact and personal info, double sided, use logo attrached please; im 42 so i need a card acording to my age an target audience.

Target Market(s)

Adult people, up scale audience

Industry/Entity Type

Music Download

Contact Information for Business Card

Cel (318) 5024471963 www.kelvarodun.com

Requirements
Must have
• open mind
Nice to have
• open mind
Should not have
• DJ

```html
<!DOCTYPE html>
<html lang="en">
<head>
<meta charset="utf-8">
<title>Kelvaro Business Card</title>
<link href="https://fonts.googleapis.com/css2?family=Arimo:wght@400;700&display=swap" rel="stylesheet">
<style>
  :root {
    --backdrop: #2b2b2b;
    --card-white: #f4f4f4;
    --card-black: #0c0c0c;
    --band-grey: #9a9a9a;
    --logo-ink: #3a3a3a;
    --text-light: #f2f2f2;
    --text-muted: #c9c9c9;
  }
  * { margin: 0; padding: 0; box-sizing: border-box; }
  html, body { width: 1200px; height: 929px; overflow: hidden; }
  body {
    background: var(--backdrop);
    font-family: "Arimo", Arial, sans-serif;
    position: relative;
  }
  .card {
    position: absolute;
    left: 250px;
    width: 700px;
    height: 400px;
    background: var(--card-white);
    overflow: hidden;
  }
  .card--front { top: 40px; }
  .card--back { top: 489px; }
  .brand {
    position: absolute;
    left: 0; right: 0;
    text-align: center;
    font-weight: 700;
    color: var(--logo-ink);
    letter-spacing: 6px;
  }
  .card--front .brand { top: 160px; font-size: 72px; }
  .card--back .brand { top: 62px; font-size: 64px; }
  .card__base { position: absolute; inset: 0; }
  .identity {
    position: absolute;
    left: 44px;
    top: 300px;
    color: var(--text-light);
  }
  .identity__name { font-size: 28px; font-weight: 700; }
  .identity__title { font-size: 19px; color: var(--text-muted); margin-top: 6px; }
  .divider {
    position: absolute;
    left: 318px;
    top: 262px;
    width: 2px;
    height: 110px;
    background: var(--text-muted);
  }
  .contacts {
    position: absolute;
    left: 345px;
    top: 258px;
    list-style: none;
    color: var(--text-light);
    font-size: 17px;
  }
  .contacts li {
    display: flex;
    align-items: center;
    gap: 12px;
    height: 29px;
  }
  .contacts svg { width: 16px; height: 16px; flex: none; }
</style>
</head>
<body>

  <section class="card card--front">
    <div class="brand">KELVARO</div>
  </section>

  <section class="card card--back">
    <svg class="card__base" viewBox="0 0 700 400" preserveAspectRatio="none" aria-hidden="true">
      <path d="M0 232 Q330 190 700 198 L700 400 L0 400 Z" fill="var(--band-grey)"/>
      <path d="M0 244 Q330 204 700 212 L700 400 L0 400 Z" fill="var(--card-black)"/>
    </svg>

    <div class="brand">KELVARO</div>

    <div class="identity">
      <div class="identity__name">Marcus Delaney</div>
      <div class="identity__title">Managing Director</div>
    </div>

    <div class="divider"></div>

    <ul class="contacts">
      <li>
        <svg viewBox="0 0 16 16"><rect width="16" height="16" rx="2" fill="#fff"/><path d="M4 4h3l1 3-1.5 1a6 6 0 0 0 2 2L10 9l3 1v2a1 1 0 0 1-1 1A9 9 0 0 1 3 5a1 1 0 0 1 1-1z" fill="#111"/></svg>
        (318) 5024471963
      </li>
      <li>
        <svg viewBox="0 0 16 16"><rect width="16" height="16" rx="2" fill="#fff"/><circle cx="8" cy="8" r="4.5" fill="none" stroke="#111" stroke-width="1.4"/><path d="M3.5 8h9M8 3.5v9" stroke="#111" stroke-width="1"/></svg>
        www.kelvarodun.com
      </li>
      <li>
        <svg viewBox="0 0 16 16"><rect width="16" height="16" rx="2" fill="#fff"/><rect x="3" y="4.5" width="10" height="7" fill="none" stroke="#111" stroke-width="1.3"/><path d="M3 4.5l5 4 5-4" fill="none" stroke="#111" stroke-width="1.3"/></svg>
        info@kelvarodun.com
      </li>
      <li>
        <svg viewBox="0 0 16 16"><rect width="16" height="16" rx="2" fill="#fff"/><path d="M8 13s-4-4.2-4-6.8a4 4 0 0 1 8 0C12 8.8 8 13 8 13z" fill="#111"/><circle cx="8" cy="6.3" r="1.4" fill="#fff"/></svg>
        47 Harlow St, Suite Brookfield MA 0218
      </li>
    </ul>
  </section>

</body>
</html>
```